Velvet Lantern rebranding my business with a new business card

I have my new logo and now I need a refresher on my business cards. I really want something fun and fresh. I like black background or anything to make the color pop.
Logo
Name: Velvet Lantern
Contact Info as stated below:
Mara Pelkin
519-555-0147
Logo
Name: Velvet Lantern
Mara Pelkin
519-555-0147
fb.me/VelvetLanternbyMara
Instagram: @VelvetLanternbyMara

Industry/Entity Type

Business

Contact Information for Business Card

double-sided. Logo on one side. Contact info on the other.

Requirements
Must have
• Logo
• Name: Velvet Lantern
• Contact Info as stated below:
• Mara Pelkin
• 519-555-0147
• fb.me/VelvetLanternbyMara
• fb.me/VelvetLanternbyMara

```html
<!DOCTYPE html>
<html lang="en">
<head>
<meta charset="utf-8">
<title>Velvet Lantern – Business Card</title>
<link href="https://fonts.googleapis.com/css2?family=Montserrat:wght@400;500&family=Open+Sans:wght@400&display=swap" rel="stylesheet">
<style>
  :root {
    --stage: #1c1c1e;
    --card-white: #ffffff;
    --card-pink: #d97eb3;
    --card-pink-deep: #c96aa2;
    --teal: #2bb0a0;
    --divider: #d9534f;
    --ink: #2a2a2a;
    --ink-soft: #5a5a5a;
    --ring: #3a3a3a;
    --ring-pink: #e9a9c8;
  }
  * { box-sizing: border-box; margin: 0; padding: 0; }
  html, body { width: 1200px; height: 963px; overflow: hidden; }
  body {
    background: var(--stage);
    position: relative;
    font-family: "Open Sans", sans-serif;
  }
  .card {
    position: absolute;
    top: 333px;
    width: 520px;
    height: 297px;
    border-radius: 14px;
  }
  .card--front { left: 60px; background: var(--card-white); }
  .card--back {
    left: 620px;
    background: linear-gradient(135deg, var(--card-pink) 0%, var(--card-pink-deep) 100%);
  }
  .logo-badge {
    position: absolute;
    width: 150px;
    height: 150px;
    border-radius: 50%;
    border: 2px solid var(--ring);
    box-shadow: inset 0 0 0 5px var(--ring-pink);
    display: flex;
    align-items: center;
    justify-content: center;
    text-align: center;
    font-family: "Montserrat", sans-serif;
    font-weight: 500;
    font-size: 17px;
    line-height: 1.25;
    letter-spacing: 1px;
    text-transform: uppercase;
    color: var(--ink);
  }
  .card--front .logo-badge { left: 70px; top: 73px; background: var(--card-white); }
  .card--back .logo-badge { left: 185px; top: 73px; }
  .divider {
    position: absolute;
    left: 262px;
    top: 80px;
    width: 2px;
    height: 137px;
    background: var(--divider);
  }
  .contact {
    position: absolute;
    left: 285px;
    top: 92px;
  }
  .contact__name {
    font-family: "Montserrat", sans-serif;
    font-weight: 400;
    font-size: 21px;
    letter-spacing: 2px;
    text-transform: uppercase;
    color: var(--teal);
    line-height: 1;
  }
  .contact__role {
    font-size: 13px;
    color: var(--ink);
    margin-top: 4px;
  }
  .contact__list {
    list-style: none;
    margin-top: 14px;
  }
  .contact__item {
    display: flex;
    align-items: center;
    gap: 10px;
    font-size: 13.5px;
    color: var(--ink-soft);
    line-height: 22px;
  }
  .contact__icon { width: 12px; height: 12px; flex: none; }
</style>
</head>
<body>
  <section class="card card--front" aria-label="Business card, contact side">
    <div class="logo-badge">Velvet<br>Lantern</div>
    <div class="divider"></div>
    <div class="contact">
      <p class="contact__name">Mara Pelkin</p>
      <p class="contact__role">Owner</p>
      <ul class="contact__list">
        <li class="contact__item">
          <svg class="contact__icon" viewBox="0 0 12 12" aria-hidden="true">
            <rect x="3" y="0.8" width="6" height="10.4" rx="1" fill="none" stroke="#2bb0a0" stroke-width="1.2"/>
            <line x1="5" y1="9.3" x2="7" y2="9.3" stroke="#2bb0a0" stroke-width="1"/>
          </svg>
          519-555-0147
        </li>
        <li class="contact__item">
          <svg class="contact__icon" viewBox="0 0 12 12" aria-hidden="true">
            <rect x="0.5" y="2" width="11" height="8" rx="1" fill="#2bb0a0"/>
            <polyline points="1,2.6 6,6.6 11,2.6" fill="none" stroke="#fff" stroke-width="1"/>
          </svg>
          info@marapelkin.com
        </li>
        <li class="contact__item">
          <svg class="contact__icon" viewBox="0 0 12 12" aria-hidden="true">
            <rect x="0.5" y="0.5" width="11" height="11" rx="2" fill="#2bb0a0"/>
          </svg>
          fb.me/VelvetLanternbyMara
        </li>
      </ul>
    </div>
  </section>

  <section class="card card--back" aria-label="Business card, logo side">
    <div class="logo-badge">Velvet<br>Lantern</div>
  </section>
</body>
</html>
```